Packaging Design Project

Hello Designers,

Our company is a new start up looking to sell rice bagged in 50kg bags and sold to africa. This packaging should show that the product is trust worthy, homely and portray a mother love and trust ie your mother know the best food for her child.

Please find enclosed our company logo enclosed(Dunmore fields) and the name of the rice is bright table. We will add later bright table gold,premium and ultra .

Front Of the bag

Top of the bag is our logo

Name: Bright Table

Picture:to be done by you

Country of origin:Vietnam Parboiled RIce

Description:100% SORTEXED

Quality:premium quality

Back of bag

Name of company:DUNMORE FIELDS

Production Date:

expiry date:

Batch number:

Origination of product:PRODUCT OF VIETNAM

Exported by : name to be provided

Reason: I would like to see more designers. We were also asked for the length and breath of the 50kg bags. length is 92cm and breath is 63cm.

WE HAVE BEEN INFORMED BY THE BAG PRINTERS THAT WE ARE LIMITED TO ONLY 3 COLOURS.PLEASE CAN YOU UPDATE YOUR DESIGNS TO JUST 3 COLORS

Target Market(s)

The target market is all women above the age of 16.

Industry/Entity Type

It Company

Requirements
Must have
• We must have a picture of an african mother preferably smiling, her age must be at least 50 to 60 years of age.

```html
<!DOCTYPE html>
<html lang="en">
<head>
<meta charset="utf-8">
<title>Bright Table – Vietnam Parboiled Rice Bag Front</title>
<link rel="stylesheet" href="https://fonts.googleapis.com/css2?family=Archivo+Black&family=Bitter:wght@800&family=Open+Sans:wght@700&family=PT+Sans+Narrow&display=swap">
<style>
  :root {
    --sky: #4aa6e6;
    --sky-light: #6cbaf0;
    --navy: #16305f;
    --navy-deep: #0f2850;
    --sun: #ffd21a;
    --badge: #fff53d;
    --orange: #f2780f;
    --orange-edge: #9a3a05;
    --rice: #f4f4f1;
    --white: #ffffff;
    --canvas: #ffffff;
  }
  * { box-sizing: border-box; margin: 0; padding: 0; }
  html, body {
    width: 1200px; height: 800px; overflow: hidden;
    background: var(--canvas);
  }
  .stage { position: relative; width: 1200px; height: 800px; }

  .bag-front {
    position: absolute; left: 317px; top: 0;
    width: 565px; height: 800px;
    background: radial-gradient(circle at 50% 40%, var(--sky-light), var(--sky) 70%);
    overflow: hidden;
  }

  .top-band {
    position: absolute; top: 48px; height: 28px; background: var(--sun);
  }
  .top-band--left { left: 0; width: 83px; }
  .top-band--right { right: 0; width: 83px; }

  .brand {
    position: absolute; top: 46px; left: 100px;
    display: flex; align-items: center; gap: 8px;
  }
  .brand__dot {
    width: 24px; height: 24px; border-radius: 50%; background: var(--navy);
  }
  .brand__name {
    font-family: "Archivo Black", sans-serif;
    font-size: 25px; letter-spacing: 1.5px; color: var(--navy);
  }

  .rice-shadow {
    position: absolute; left: 210px; top: 195px; width: 302px; height: 455px;
    border-radius: 40px; background: var(--navy-deep);
  }
  .rice-panel {
    position: absolute; left: 180px; top: 102px; width: 318px; height: 538px;
    border-radius: 40px;
    background: linear-gradient(160deg, var(--white), var(--rice) 60%, #e6e6e2);
  }
  .quality-line {
    position: absolute; left: 450px; top: 400px;
    transform: translate(-50%, -50%) rotate(-90deg);
    font-family: "PT Sans Narrow", sans-serif;
    font-size: 27px; color: var(--navy); white-space: nowrap;
  }

  .family-photo {
    position: absolute; left: 33px; top: 140px; width: 330px; height: 410px;
    border-radius: 62px;
    background: linear-gradient(170deg, #b88a5e 0%, #8a5a3a 40%, #6a3e28 75%, #4a2c22 100%);
    box-shadow: 0 0 18px 6px rgba(255,255,255,0.85);
  }

  .sortex-badge {
    position: absolute; left: 400px; top: 104px; width: 124px; height: 90px;
  }
  .sortex-badge svg { position: absolute; inset: 0; }
  .sortex-badge__text {
    position: absolute; inset: 0; display: flex; flex-direction: column;
    align-items: center; justify-content: center; transform: rotate(-6deg);
  }
  .sortex-badge__pct {
    font-family: "Bitter", serif; font-weight: 800;
    font-size: 30px; line-height: 1; color: var(--navy);
  }
  .sortex-badge__word {
    font-family: "PT Sans Narrow", sans-serif;
    font-size: 22px; line-height: 1; color: #2a6fb8;
  }

  .title-plate {
    position: absolute; left: 85px; top: 526px; width: 380px; height: 188px;
    border-radius: 48px; background: var(--white);
    box-shadow: 0 0 20px 8px rgba(255,255,255,0.7);
  }
  .product-name {
    position: absolute; left: 85px; top: 532px; width: 380px;
    text-align: center;
    font-family: "Bitter", serif; font-weight: 800;
    color: var(--orange); line-height: 0.95;
    text-shadow: 2px 2px 0 var(--orange-edge);
  }
  .product-name span { display: block; }
  .product-name__first { font-size: 66px; }
  .product-name__second { font-size: 74px; }

  .origin {
    position: absolute; left: 200px; top: 725px;
    font-family: "Open Sans", sans-serif; font-weight: 700;
    font-size: 18px; color: var(--navy);
  }
</style>
</head>
<body>
<main class="stage">
  <section class="bag-front">
    <div class="top-band top-band--left"></div>
    <div class="top-band top-band--right"></div>
    <div class="brand">
      <span class="brand__dot"></span>
      <span class="brand__name">DUNMORE FIELDS</span>
    </div>

    <div class="rice-shadow"></div>
    <div class="rice-panel" role="img" aria-label="Close-up of white parboiled rice grains"></div>
    <p class="quality-line">Premium Quality Rice</p>

    <div class="family-photo" role="img" aria-label="Photo of a smiling African mother hugging her young daughter"></div>

    <div class="sortex-badge">
      <svg viewBox="0 0 124 90" width="124" height="90" aria-hidden="true">
        <path d="M20 30 C18 10 45 4 58 12 C70 0 100 4 104 22 C122 26 124 52 110 62 C112 80 86 90 70 80 C56 92 28 88 24 72 C4 70 0 40 20 30 Z" fill="var(--badge)"/>
      </svg>
      <div class="sortex-badge__text">
        <span class="sortex-badge__pct">100%</span>
        <span class="sortex-badge__word">Sortexed</span>
      </div>
    </div>

    <div class="title-plate"></div>
    <h1 class="product-name">
      <span class="product-name__first">BRIGHT</span>
      <span class="product-name__second">TABLE</span>
    </h1>
    <p class="origin">Vietnam Parboiled RIce</p>
  </section>
</main>
</body>
</html>
```